Elegant, Playful, Health And Wellness Packaging Design for an Essential Oil Diffuser

Box design for diffuser, should be elegant, luxury, white box with gold foil and vibrant color combination that pops off the white box.

Designs look the same

```html
<!DOCTYPE html>
<html lang="en">
<head>
<meta charset="utf-8">
<title>Aurelle Ultrasonic Diffuser – Carton Dieline</title>
<link href="https://fonts.googleapis.com/css2?family=Arimo:wght@400;700&family=Great+Vibes&display=swap" rel="stylesheet">
<style>
  :root {
    --gold: #b38a27;
    --gold-light: #c9a13d;
    --gold-pale: #e9dcb4;
    --green: #3f9b2c;
    --grey: #6d6e70;
    --ink: #1a1a1a;
    --cut: #e0197d;
    --paper: #ffffff;
  }
  * { box-sizing: border-box; margin: 0; padding: 0; }
  html, body { width: 1200px; height: 1200px; overflow: hidden; background: var(--paper); }
  body { position: relative; font-family: "Arimo", Arial, sans-serif; }

  .dieline {
    position: absolute; left: 22px; top: 229px;
    width: 1410px; height: 905px;
    transform: scale(0.82); transform-origin: 0 0;
  }
  .dieline__cut { position: absolute; inset: 0; width: 1410px; height: 905px; }
  .dieline__cut path, .dieline__cut line { fill: none; stroke: var(--cut); stroke-width: 2; }

  .panel { position: absolute; top: 395px; height: 277px; width: 352px; text-align: center; }
  .panel--side { left: 0; }
  .panel--front { left: 353px; }
  .panel--info { left: 705px; text-align: left; }
  .panel--back { left: 1055px; }

  .pattern-field {
    position: absolute; inset: 2px 0 2px 2px;
    background: repeating-linear-gradient(90deg, var(--gold-light) 0 3px, var(--gold-pale) 3px 6px);
  }
  .side-block {
    position: absolute; left: 75px; top: 88px; width: 200px; height: 186px;
    background: var(--gold); color: #fff;
  }
  .side-block__ring {
    width: 70px; height: 70px; border: 3px solid #fff; border-radius: 50%;
    margin: 26px auto 10px;
  }
  .side-block__name { font-weight: 700; font-size: 27px; letter-spacing: 2px; }
  .side-block__url { font-size: 12px; margin-top: 30px; }

  .tagline {
    font-family: "Great Vibes", cursive; color: var(--gold);
    font-size: 22px; margin-top: 20px; letter-spacing: 0.5px;
  }
  .brand-ring {
    width: 78px; height: 78px; border-radius: 50%; margin: 18px auto 8px;
    border: 6px solid var(--gold);
  }
  .brand-name { color: var(--gold); font-weight: 700; font-size: 30px; letter-spacing: 3px; line-height: 1; }
  .brand-sub { color: var(--grey); font-size: 14px; margin-top: 6px; }
  .product-type { font-size: 12.5px; margin-top: 30px; }
  .product-type--green { color: var(--green); }
  .product-type--black { color: var(--ink); }

  .info { position: absolute; left: 52px; top: 52px; width: 250px; color: var(--grey); font-size: 8.4px; line-height: 1.32; }
  .info__title { color: var(--green); font-weight: 700; font-size: 9.6px; }
  .info__body { text-align: justify; }
  .info__cols { display: flex; gap: 28px; margin-top: 18px; }
  .info__head { color: var(--green); font-weight: 700; font-size: 10px; margin-bottom: 2px; }
  .features { list-style: none; width: 110px; }
  .features li::before { content: "• "; color: var(--green); }
  .specs { list-style: none; width: 122px; }
  .specs li { border-bottom: 1px dotted var(--green); padding: 0.5px 0; }

  .lid { position: absolute; left: 353px; top: 42px; width: 352px; height: 353px; }
  .lid__ring {
    position: absolute; left: 82px; top: 110px; width: 188px; height: 188px;
    border: 12px solid var(--ink); border-radius: 50%;
    display: flex; align-items: center; justify-content: center;
  }
  .lid__name { color: var(--ink); font-weight: 700; font-size: 26px; letter-spacing: 2px; }
</style>
</head>
<body>
  <main class="dieline">
    <svg class="dieline__cut" viewBox="0 0 1410 905" aria-hidden="true">
      <path d="M0 395 H1408 V672 H0 Z"/>
      <line x1="353" y1="395" x2="353" y2="672"/>
      <line x1="705" y1="395" x2="705" y2="672"/>
      <line x1="1055" y1="395" x2="1055" y2="672"/>
      <path d="M353 395 V25 Q353 5 373 5 H685 Q705 5 705 25 V395"/>
      <line x1="353" y1="42" x2="705" y2="42"/>
      <path d="M0 395 V365 L40 240 Q48 218 70 218 H330 Q342 218 342 230 V380 L353 395"/>
      <path d="M705 395 L715 380 V230 Q715 218 727 218 H985 Q1007 218 1015 240 L1055 365 V395"/>
      <path d="M1178 395 V365 Q1178 355 1188 355 H1274 Q1284 355 1284 365 V395"/>
      <path d="M0 672 V838 Q0 845 8 845 H168 Q176 845 176 838 V755 L353 672"/>
      <path d="M353 672 V895 H438 V848 H618 V895 H705 V672"/>
      <path d="M705 672 L880 755 V838 Q880 845 888 845 H1048 Q1055 845 1055 838 V672"/>
      <path d="M1055 672 L1140 895 H1320 L1408 672"/>
    </svg>

    <section class="lid">
      <div class="lid__ring"><span class="lid__name">AURELLE</span></div>
    </section>

    <section class="panel panel--side">
      <div class="pattern-field" role="img" aria-label="Gold meander pattern covering the side panel"></div>
      <div class="side-block">
        <div class="side-block__ring"></div>
        <div class="side-block__name">AURELLE</div>
        <div class="side-block__url">www.aurelle-oils.com</div>
      </div>
    </section>

    <section class="panel panel--front">
      <p class="tagline">Experience the Essence of Nature</p>
      <div class="brand-ring"></div>
      <p class="brand-name">AURELLE</p>
      <p class="brand-sub">Heritage Botanical Collection</p>
      <p class="product-type product-type--green">Ultrasonic Diffuser</p>
    </section>

    <section class="panel panel--info">
      <div class="info">
        <p class="info__title">AURELLE BOTANICAL OILS DIFFUSER</p>
        <p class="info__body">Experience the pure essence of nature with the Aurelle Lumo Diffuser. Sourced from the farthest reaches of the earth, Aurelle Botanical Oils are extracted only from the highest quality and purest raw form ingredients. Using the Lumo diffuser with Aurelle Botanical Oils can help improve health, quality of life, and overall spiritual balance.</p>
        <div class="info__cols">
          <div>
            <p class="info__head">Features</p>
            <ul class="features">
              <li>Continuous diffusing</li>
              <li>Timer settings</li>
              <li>7 LED color &amp; light settings</li>
              <li>Portable</li>
              <li>Pet safe</li>
              <li>Easy to clean</li>
            </ul>
          </div>
          <div>
            <p class="info__head">Specifications</p>
            <ul class="specs">
              <li>Dimensions: 135*135*108mm</li>
              <li>Capacity: 300ml</li>
              <li>33 ml/hour output</li>
              <li>Safety Auto-off when empty</li>
              <li>Whisper Quiet</li>
              <li>Contains 1 Lumo Diffuser,<br>1 Power Adaptor</li>
            </ul>
          </div>
        </div>
      </div>
    </section>

    <section class="panel panel--back">
      <p class="tagline">Experience the Essence of Nature</p>
      <div class="brand-ring"></div>
      <p class="brand-name">AURELLE</p>
      <p class="brand-sub">Heritage Botanical Collection</p>
      <p class="product-type product-type--black">Ultrasonic Diffuser</p>
    </section>
  </main>
</body>
</html>
```